Existing company needs Rebranding on logo and website!!

the company is called fund in Kenya (www.plorvexatrade.co.uk) check the site to see the existing site and logo, this has to change and must be completely different.

I want to the turn the website into a crowd funding site, but i want an inovative and interacive site. Have a look http://www.zentro.org/about/how or https://www.boldmuvi.com/ to get an idea of what is required. However i do not want my site to be anything like this. It is 2015 so web browser can do alot. when it comes to selecting project proposals on the site i want them them to pop up use your imagination your the desgner. ofcourse the site will be taking card payments and possibly bank transfers and maybe quidnest. the usual API are already on the site so you wont need to do much. the site is hosted by pagebloom so i do prefer it to stay there. i am familiar with that platform.

interms of creativity you have full control we wil be working closely and i expect to be kept in the loop as things develope.

the site will also need to be turn into a mobile app which serves different purposes depending if your an investor or project sponsor.

i will give you all the information required we can communicate on talvox email or telephone i am flexible.

many thanks

Target Market(s)

Investors

Industry/Entity Type

Finance

Number of Pages Required

5+ page

Font styles to use
Sans Serif

Colors
3176b5
f04a50
abd036
00a990

Requirements
Must have
• i want the designer to look at my existing site www.plorvexatrade.co.uk and come up with a better design concept.

```html
<!DOCTYPE html>
<html lang="en">
<head>
<meta charset="utf-8">
<title>fund in Kenya — Crowdfunding for innovative businesses</title>
<link href="https://fonts.googleapis.com/css2?family=Open+Sans:wght@300;400;600;700&display=swap" rel="stylesheet">
<style>
:root{
  --teal:#00a990;
  --lime:#abd036;
  --lime-dark:#95b82a;
  --blue:#3176b5;
  --navy:#1d4f8e;
  --red:#f04a50;
  --ink:#333;
  --heading:#444;
  --muted:#777;
  --pale:#dff5f7;
  --line:#e3e3e3;
}
*{margin:0;padding:0;box-sizing:border-box}
html,body{width:1200px;height:2188px;overflow:hidden}
body{font-family:"Open Sans",Arial,sans-serif;color:var(--ink);background:#fff}
.page{width:1200px;height:2188px;position:relative}

/* header */
.site-header{height:104px;position:relative}
.brand{position:absolute;left:96px;top:30px;display:flex;align-items:center;gap:12px}
.brand-mark{width:30px;height:30px;background:var(--teal)}
.brand-name{font-size:34px;font-weight:600;color:var(--teal);letter-spacing:-.5px}
.account{position:absolute;right:96px;top:46px;display:flex;gap:12px}
.account a{display:block;width:80px;height:26px;line-height:26px;text-align:center;font-size:12px;font-weight:600;color:#fff;text-decoration:none}
.btn-signup{background:var(--teal)}
.btn-login{background:#9a9a9a}

.main-nav{height:36px;background:var(--lime);display:flex;align-items:center;padding-left:110px}
.main-nav a{font-size:13px;font-weight:600;color:#fff;text-decoration:none;text-transform:uppercase;padding:0 24px;line-height:36px}
.main-nav a.active{background:var(--lime-dark)}

/* hero */
.hero{position:relative;height:420px}
.hero-photo{position:absolute;inset:0;background:linear-gradient(100deg,#6d7f86 0%,#c9d3d4 30%,#eef1f0 55%,#a9b6b3 100%)}
.hero-card{position:absolute;left:680px;top:108px;width:392px;height:200px;background:rgba(0,169,144,.9);padding:22px 30px;color:#fff}
.hero-card h1{font-weight:700;font-size:58px;line-height:1}
.hero-card .accent{font-weight:300;font-size:62px;line-height:1.05;color:#e8fff9}
.hero-card p{font-size:28px;font-weight:300;color:#d6f2ea;margin-top:4px}

/* welcome */
.welcome{text-align:center;padding:48px 160px 0}
.welcome h2{font-size:46px;font-weight:300;color:var(--heading)}
.welcome p{font-size:13px;line-height:1.6;color:var(--muted);margin-top:18px}
.welcome p+p{margin-top:12px}

/* features */
.features{position:absolute;top:848px;left:0;width:1200px;height:264px;background:var(--teal);display:flex;justify-content:center;gap:140px;padding-top:44px}
.feature{text-align:center;width:130px;color:#fff}
.feature-icon{width:120px;height:120px;border-radius:50%;background:var(--lime);border:8px solid #0fbfa3;margin:0 auto;display:flex;align-items:center;justify-content:center}
.feature h3{font-size:22px;font-weight:700;margin-top:24px;white-space:nowrap}

/* projects & news */
.info{position:absolute;top:1140px;left:96px;width:1008px;display:flex;gap:60px}
.section-title{font-size:38px;font-weight:300;color:var(--lime);border-bottom:1px solid var(--line);padding-bottom:6px}
.services{width:620px}
.tabs{display:flex;margin-top:18px;border-bottom:1px solid var(--line)}
.tabs span{padding:12px 26px;font-size:16px;color:#555}
.tabs span.active{border:1px solid var(--line);border-bottom:1px solid #fff;margin-bottom:-1px;color:#222}
.service-body{display:flex;gap:22px;margin-top:24px}
.service-photo{width:170px;height:160px;background:linear-gradient(135deg,#8ea7b9,#d5dfe6);flex:none}
.service-body p{font-size:12px;line-height:1.6;color:var(--muted);width:200px}
.news{width:328px}
.news p{font-size:12px;line-height:1.6;color:var(--muted)}
.news .lead{font-weight:600;color:#555;margin-top:18px}
.news .gap{margin-top:22px}

/* testimonials */
.testimonials-title{position:absolute;top:1616px;width:1200px;text-align:center;font-size:40px;font-weight:300;color:var(--heading)}
.testimonials{position:absolute;top:1688px;left:0;width:1200px;height:412px;background:var(--pale)}
.quote-card{position:absolute;left:200px;top:24px;width:800px;height:200px;background:#fff;border-top:1px solid #cfe3e6;border-bottom:1px solid #cfe3e6;text-align:center;padding-top:50px}
.quote-mark{position:absolute;left:50%;top:-6px;transform:translateX(-50%);width:80px;height:56px;background:var(--pale);display:flex;align-items:center;justify-content:center}
.quote-card h4{font-size:14px;font-weight:400;color:var(--blue)}
.quote-card p{font-size:12px;color:var(--muted);line-height:1.6;margin:10px auto 0;width:560px}
.quote-card .author{color:var(--blue);font-weight:600;margin-top:12px}
.quote-card .role{margin-top:0;font-size:11px}
.dots{position:absolute;top:244px;left:0;width:1200px;display:flex;justify-content:center;gap:10px}
.dots i{width:12px;height:12px;border-radius:50%;background:#8fb9d6}
.dots i.on{background:var(--blue)}
.cta{position:absolute;top:274px;width:1200px;text-align:center}
.cta h3{font-size:34px;font-weight:300;color:var(--heading)}
.cta p{font-size:13px;color:var(--muted);margin-top:6px}
.cta a{display:inline-block;margin-top:16px;width:196px;height:48px;line-height:48px;background:var(--teal);color:#fff;font-size:18px;text-decoration:none}

/* footer */
.site-footer{position:absolute;bottom:0;left:0;width:1200px;height:88px;background:var(--navy);color:#fff;text-align:center;padding-top:24px}
.site-footer nav{font-size:12px}
.site-footer nav a{color:#fff;text-decoration:none;margin:0 10px}
.site-footer small{display:block;font-size:11px;color:#c7d6ea;margin-top:8px}
</style>
</head>
<body>
<div class="page">
  <header class="site-header">
    <div class="brand"><span class="brand-mark"></span><span class="brand-name">fund in Kenya</span></div>
    <div class="account"><a class="btn-signup" href="#">SIGN UP</a><a class="btn-login" href="#">LOG IN</a></div>
  </header>
  <nav class="main-nav">
    <a class="active" href="#">Home</a><a href="#">About Us</a><a href="#">Company Profile</a><a href="#">They Trust Us</a><a href="#">Management Team</a><a href="#">Partners</a><a href="#">Contact Us</a>
  </nav>

  <section class="hero">
    <div class="hero-photo" role="img" aria-label="Business team meeting around a table in a bright office"></div>
    <div class="hero-card">
      <h1>Invest in</h1>
      <div class="accent">innovative</div>
      <p>British businesses</p>
    </div>
  </section>

  <section class="welcome">
    <h2>Welcome fund in Kenya</h2>
    <p>fund in Kenya is a crowdfunding platform that connects investors with innovative, growing businesses. Browse live project proposals, open any one to see its full pitch, and back the ideas you believe in with as little or as much as you like.</p>
    <p>fund in Kenya works with its partners to check every proposal before it goes live, so investors see clear goals, honest figures and regular updates. Pay securely by card or bank transfer, follow each project's progress from your dashboard, and share the projects you back with friends to help them reach their target sooner.</p>
  </section>

  <section class="features">
    <div class="feature">
      <div class="feature-icon"><svg width="48" height="48" viewBox="0 0 48 48" fill="none" stroke="#fff" stroke-width="4" stroke-linecap="round" stroke-linejoin="round"><path d="M18 40V14a4 4 0 0 1 8 0v12l10 2a4 4 0 0 1 3 5l-3 7z"/></svg></div>
      <h3>Advantage</h3>
    </div>
    <div class="feature">
      <div class="feature-icon"><svg width="56" height="48" viewBox="0 0 56 48" fill="none" stroke="#fff" stroke-width="4" stroke-linecap="round" stroke-linejoin="round"><path d="M4 18l10-6 10 4 8-4 10 2 10 6"/><path d="M14 26l10 10 4-2 4 2 8-8"/><path d="M24 16l-6 8 8 4 8-8"/></svg></div>
      <h3>Interoperability</h3>
    </div>
    <div class="feature">
      <div class="feature-icon"><svg width="50" height="48" viewBox="0 0 50 48" fill="none" stroke="#fff" stroke-width="4" stroke-linecap="round"><path d="M6 42h38"/><path d="M12 36V26M22 36V18M32 36V22M42 36V10"/></svg></div>
      <h3>Solution</h3>
    </div>
    <div class="feature">
      <div class="feature-icon"><svg width="48" height="48" viewBox="0 0 48 48" fill="none" stroke="#fff" stroke-width="4" stroke-linecap="round"><circle cx="24" cy="24" r="8"/><path d="M24 4v7M24 37v7M4 24h7M37 24h7M10 10l5 5M33 33l5 5M38 10l-5 5M15 33l-5 5"/></svg></div>
      <h3>Technology</h3>
    </div>
  </section>

  <section class="info">
    <div class="services">
      <h2 class="section-title">services</h2>
      <div class="tabs"><span class="active">Operator</span><span>Brand &amp; Content</span><span>Enterprise</span></div>
      <div class="service-body">
        <div class="service-photo" role="img" aria-label="Two business people shaking hands over a signed agreement"></div>
        <p>fund in Kenya helps project sponsors launch and run their campaigns. We review each proposal, shape a clear pitch and set a funding goal investors can trust. Once live, sponsors reach a wide network of backers, post updates from one dashboard and receive funds safely when their target is met.</p>
      </div>
    </div>
    <div class="news">
      <h2 class="section-title">latest news</h2>
      <p class="lead">Veltrix 360 Reaches Its Funding Goal In Ten Days With Support From Over Four Hundred Backers</p>
      <p class="gap">London, U.K. - September, 2015</p>
      <p>New projects open for backing this week</p>
      <p>Bank transfers now accepted on all pledges</p>
      <p>Investor app coming soon to your phone</p>
      <p>Sponsors can now post video updates</p>
    </div>
  </section>

  <h2 class="testimonials-title">Client Testimonials</h2>
  <section class="testimonials">
    <div class="quote-card">
      <div class="quote-mark"><svg width="40" height="30" viewBox="0 0 40 30" fill="#3176b5"><path d="M2 30V16C2 6 8 1 16 0v6c-4 1-7 4-7 9h7v15zM22 30V16c0-10 6-15 14-16v6c-4 1-7 4-7 9h7v15z"/></svg></div>
      <h4>Brightpath Tutor Search</h4>
      <p>We needed funding to grow our tutoring service. Within weeks our proposal was live, backers found us quickly and we reached our goal with support to spare.</p>
      <p class="author">Marisol Teviot</p>
      <p class="role">Unit 14, Phase 2, Riverside</p>
    </div>
    <div class="dots"><i class="on"></i><i></i><i></i></div>
    <div class="cta">
      <h3>Discover great projects with your friends!</h3>
      <p>Over a thousand investors have already found their right projects through us!</p>
      <a href="#">Learn More</a>
    </div>
  </section>

  <footer class="site-footer">
    <nav><a href="#">Home</a>|<a href="#">About</a>|<a href="#">Product</a>|<a href="#">Quality</a>|<a href="#">Contact Us</a></nav>
    <small>Copyright © 2015. All Rights Reserved | Privacy Policy</small>
  </footer>
</div>
</body>
</html>
```